Uprising SaaS company needs an attractive business card design

We're an uprising SaaS company who's attempting to attack the rigid car (insurance) claims management market in Europe.
We want to our mighty base order management system, listen to our clients to connect the smart ideas to build something even mightier.
We primarily focus on helping our customers manage their customers' claims/orders and get them resolved as smoothly as possible.
We'd like the business card design to express technical innovation and the fact that we connect smart ideas, as our company slogan indicates.
Contact Information for Business Card
Name, position, website, email, mobile, business address
Font styles to use
Colors
Designer to choose colors to be used in the design.
Look and feel
Each slider illustrates characteristics of the customer's brand and the style your logo design should communicate.

```html
<!DOCTYPE html>
<html lang="en">
<head>
<meta charset="utf-8">
<title>Claimora business card</title>
<link href="https://fonts.googleapis.com/css2?family=Montserrat:wght@400;700&display=swap" rel="stylesheet">
<style>
  :root{
    --stage:#b3b3b3;
    --card-dark:#232323;
    --card-light:#ffffff;
    --brand-grey:#7a7a7a;
    --brand-grey-dark:#4a4a4a;
    --accent:#7ccbe3;
    --ink:#1e1e1e;
  }
  *{margin:0;padding:0;box-sizing:border-box}
  html,body{width:1200px;height:900px;overflow:hidden}
  body{
    background:var(--stage);
    font-family:'Montserrat',Arial,sans-serif;
    display:flex;flex-direction:column;align-items:center;justify-content:center;gap:60px;
  }
  .card{
    width:620px;height:355px;border-radius:18px;
    box-shadow:0 10px 28px rgba(0,0,0,.25);
    position:relative;overflow:hidden;
  }
  .card--back{background:var(--card-dark);display:flex;align-items:center;justify-content:center}
  .card--back .wordmark{color:var(--brand-grey-dark);font-size:78px}
  .card--front{background:var(--card-light);display:flex;align-items:center;padding:0 40px 0 50px}
  .wordmark{
    font-family:'Montserrat',Arial,sans-serif;font-weight:400;
    letter-spacing:1px;display:flex;align-items:center;gap:12px;line-height:1;
  }
  .wordmark__dot{width:12px;height:12px;border-radius:50%;background:currentColor;display:inline-block}
  .card--front .wordmark{color:var(--brand-grey);font-size:56px;flex:0 0 auto}
  .divider{width:2px;height:190px;background:var(--accent);margin:0 28px 0 34px;flex:0 0 auto}
  .contact{color:var(--ink);font-size:14px}
  .contact__name{color:var(--accent);font-weight:700;font-size:22px;line-height:1.1}
  .contact__role{font-size:14px;margin-bottom:14px}
  .contact__list{list-style:none;margin-bottom:14px}
  .contact__list li{display:flex;align-items:center;gap:10px;line-height:1.45}
  .contact__list svg{width:13px;height:13px;fill:var(--accent);flex:0 0 auto}
  .contact__address{font-style:normal;line-height:1.35}
</style>
</head>
<body>
  <section class="card card--back" aria-label="Card back">
    <div class="wordmark">claimora<span class="wordmark__dot"></span></div>
  </section>

  <section class="card card--front" aria-label="Card front">
    <div class="wordmark">claimora</div>
    <div class="divider"></div>
    <div class="contact">
      <p class="contact__name">Lena Marquardt</p>
      <p class="contact__role">CEO</p>
      <ul class="contact__list">
        <li><svg viewBox="0 0 16 16"><path d="M3 1h3l1.5 4-2 1.3a9 9 0 0 0 4.2 4.2L11 8.5 15 10v3a2 2 0 0 1-2 2A12 12 0 0 1 1 3a2 2 0 0 1 2-2z"/></svg>+49 170 5512340</li>
        <li><svg viewBox="0 0 16 16"><path d="M1 3h14v10H1z M1 3l7 5 7-5" stroke="#fff" stroke-width="1.2"/></svg>hello@claimora.com</li>
        <li><svg viewBox="0 0 16 16"><circle cx="8" cy="8" r="7"/><path d="M1 8h14M8 1c-3 3.5-3 10.5 0 14M8 1c3 3.5 3 10.5 0 14" stroke="#fff" stroke-width="1" fill="none"/></svg>www.claimora.com</li>
      </ul>
      <address class="contact__address">Lindenweg 14b<br>10115 Berlin, Germany</address>
    </div>
  </section>
</body>
</html>
```